Wedding Marloes & Joost - Save the Date Wedding Card

I would like to have a creative save the date wedding card. We like grey/black/white colors and modern/ plain and simple.
I like the Save the Date copy big and book a flight copy smaller. I like stylish fonts for the save the date copy
Copy front:
Save the Date & book a flight
7-10-2017 Denia (Spanje)
Marloes & Joost
Onze dag is niet compleet zonder jou!
Copy back:
6-10 preferred travel date
7-10 wedding ceremony/drinks/dinner/party
8-10 hangover breakfast
Nearest Airports Valencia & Alicante
More info will be available soon!
Target Market(s)
wedding guests
Industry/Entity Type
Wedding

```html
<!DOCTYPE html>
<html lang="nl">
<head>
<meta charset="utf-8">
<title>Save the Date – Marloes &amp; Joost</title>
<link href="https://fonts.googleapis.com/css2?family=Courgette&family=Great+Vibes&display=swap" rel="stylesheet">
<style>
  :root {
    --stage: #3a3a3a;
    --sky-top: #cfe9f8;
    --sky-mid: #a9d8f3;
    --sea: #8ccbee;
    --foam: #eef8fd;
    --sand: #f6e2bd;
    --ink: #161616;
    --dot: #ffffff;
    --couple: #d9dde0;
    --couple-dark: #8b8f93;
  }
  * { box-sizing: border-box; margin: 0; padding: 0; }
  html, body { width: 1200px; height: 1000px; overflow: hidden; }
  body {
    background: var(--stage);
    position: relative;
    font-family: "Courgette", cursive;
    color: var(--ink);
  }
  .card {
    position: absolute;
    width: 620px;
    height: 430px;
    background: linear-gradient(180deg,
      var(--sky-top) 0%,
      var(--sky-mid) 30%,
      var(--foam) 42%,
      var(--sea) 55%,
      var(--foam) 72%,
      var(--sand) 88%,
      var(--sand) 100%);
    box-shadow: 0 8px 24px rgba(0,0,0,.45);
    overflow: hidden;
  }
  .card--front { left: 150px; top: 40px; }
  .card--back  { left: 430px; top: 520px; }

  .dotted-frame {
    position: absolute;
    left: 40px; top: 40px; right: 40px; bottom: 40px;
    border: 4px dotted var(--dot);
    border-radius: 6px;
  }
  .copy {
    position: absolute;
    text-align: center;
  }
  .front-copy { top: 72px; left: 48px; width: 420px; }
  .tagline { font-size: 24px; line-height: 1.3; }
  .couple-names {
    font-family: "Great Vibes", cursive;
    font-weight: 400;
    font-size: 62px;
    line-height: 1.15;
    margin-top: 14px;
    white-space: nowrap;
  }
  .wedding-date { font-size: 30px; font-weight: 700; margin-top: 14px; line-height: 1.3; }
  .location { font-size: 18px; margin-top: 6px; line-height: 1.3; }
  .closing { font-size: 20px; margin-top: 4px; line-height: 1.3; white-space: nowrap; }

  .back-copy { top: 95px; left: 0; right: 0; font-size: 21px; line-height: 1.45; }
  .back-copy .airports { margin-top: 22px; }

  .couple-art {
    position: absolute;
    background: linear-gradient(180deg, var(--couple), var(--couple-dark));
    border-radius: 8px;
    opacity: .85;
  }
  .card--front .couple-art { left: 478px; top: 205px; width: 88px; height: 88px; }
  .card--back .couple-art { left: 260px; top: 300px; width: 120px; height: 110px; }
</style>
</head>
<body>
  <section class="card card--front" aria-label="Voorkant save the date kaart">
    <div class="dotted-frame"></div>
    <div class="copy front-copy">
      <p class="tagline">Save the Date &amp; book a flight</p>
      <h1 class="couple-names">Marloes &amp; Joost</h1>
      <p class="wedding-date">7 oktober 2017</p>
      <p class="location">Denia, Spanje</p>
      <p class="closing">Onze dag is niet compleet zonder jou!</p>
    </div>
    <div class="couple-art" role="img" aria-label="Illustratie van bruidspaar op een bankje onder een parasol met hartjes"></div>
  </section>

  <section class="card card--back" aria-label="Achterkant save the date kaart">
    <div class="copy back-copy">
      <p>6-10 Preferred travel date</p>
      <p>7-10 Wedding ceremony/drinks/dinner/party</p>
      <p>8-10 Hangover lunch</p>
      <p class="airports">Nearest Airports Valencia &amp; Alicante</p>
      <p>More info will be available soon!</p>
    </div>
    <div class="couple-art" role="img" aria-label="Illustratie van bruidspaar op een bankje onder een parasol met hartjes"></div>
  </section>
</body>
</html>
```